Banner Design for Holistic Clinic

We need a banner to be designed for a Holistic Clinic which treats patient using IV Nutrition therapy, IV Vitamin C therapy, Chelation therapy, Homoepathy , Accupuncture, Ayurveda. Our website is www.verdantcarehub.in

We need the banner to show case all our services. IV Nutrition therapy, IV Vitamin C therapy, Chelation therapy, Homoepathy , Accupuncture, Ayurveda with special emphasis on IV Therapies. This will be in the front of the web page and will be used for leaflets and flex material.Ideally

I like the concept of IV infsuion bags, fruits etc. I have attached some of the pic which i liked. Please see the attachment "banner clinic july 13" But feel free to change it and bring in something better that will showcase all our services together

Target Market(s)

30 plus Adults

Industry/Entity Type

Health And Wellness

Font styles to use
Serif

Colors
acd036
f37122
33a6d7

Requirements
Must have
• Some samples are given below. It got to be colourful, yet pleasing.

```html
<!DOCTYPE html>
<html lang="en">
<head>
<meta charset="utf-8">
<title>Verdant Care Hub – Our Services</title>
<link rel="stylesheet" href="https://fonts.googleapis.com/css2?family=Libre+Baskerville:wght@700&family=Open+Sans:wght@700;800&display=swap">
<style>
  :root {
    --page: #ffffff;
    --lime: #b7d968;
    --lime-deep: #a9cf55;
    --green-ink: #1c6b21;
    --orange: #f37122;
    --blue: #33a6d7;
    --white: #ffffff;
  }
  html, body {
    margin: 0;
    width: 1200px;
    height: 1200px;
    overflow: hidden;
    background: var(--page);
  }
  .banner {
    position: absolute;
    left: 96px;
    top: 410px;
    width: 1010px;
    height: 380px;
    overflow: hidden;
    background: var(--lime);
  }
  .banner-art { position: absolute; inset: 0; }
  .brand-credit, .brand-tagline { font-family: "Open Sans", sans-serif; font-weight: 700; font-size: 7px; fill: var(--green-ink); }
  .brand-name { font-family: "Open Sans", sans-serif; font-weight: 800; font-size: 17px; fill: var(--green-ink); letter-spacing: 0.3px; }
  .section-title { font-family: "Libre Baskerville", serif; font-weight: 700; font-size: 50px; fill: var(--green-ink); }
  .service-label { font-family: "Open Sans", sans-serif; font-weight: 800; font-size: 13.5px; fill: var(--green-ink); }
</style>
</head>
<body>
<section class="banner" aria-label="Our services banner">
  <svg class="banner-art" viewBox="0 0 1010 380" width="1010" height="380" xmlns="http://www.w3.org/2000/svg">
    <defs>
      <linearGradient id="fill-chelation" x1="0" y1="0" x2="1" y2="1"><stop offset="0" stop-color="#1b2a6b"/><stop offset="0.5" stop-color="#c0552f"/><stop offset="1" stop-color="#27337a"/></linearGradient>
      <linearGradient id="fill-vitamin" x1="0" y1="0" x2="1" y2="1"><stop offset="0" stop-color="#f59a2a"/><stop offset="1" stop-color="#e0661a"/></linearGradient>
      <linearGradient id="fill-nutrition" x1="0" y1="0" x2="1" y2="1"><stop offset="0" stop-color="#c9302a"/><stop offset="0.5" stop-color="#c9a060"/><stop offset="1" stop-color="#6aa52e"/></linearGradient>
      <linearGradient id="fill-homeopathy" x1="0" y1="0" x2="0" y2="1"><stop offset="0" stop-color="#6c8a3a"/><stop offset="1" stop-color="#efece2"/></linearGradient>
      <linearGradient id="fill-acupuncture" x1="0" y1="0" x2="1" y2="0"><stop offset="0" stop-color="#e6c0a8"/><stop offset="1" stop-color="#2a2a2e"/></linearGradient>
    </defs>

    <!-- decorative waves -->
    <path d="M640 0 C700 25 760 30 820 22 C880 14 940 40 1010 30 L1010 0 Z" fill="var(--orange)"/>
    <path d="M950 0 L1010 0 L1010 30 C985 34 965 20 950 0 Z" fill="var(--blue)"/>
    <path d="M560 0 C640 40 720 30 790 35 C870 42 930 20 1010 50" fill="none" stroke="var(--blue)" stroke-width="1.5"/>
    <path d="M600 0 C680 30 760 55 850 40 C920 28 960 55 1010 60" fill="none" stroke="var(--orange)" stroke-width="1.5"/>
    <path d="M0 260 C40 250 60 300 110 320 C150 338 180 360 240 380 L0 380 Z" fill="var(--orange)"/>
    <path d="M0 240 C15 250 20 270 18 300 C10 290 0 285 0 285 Z" fill="var(--blue)"/>
    <path d="M0 160 C40 180 30 250 80 290 C120 320 170 330 210 380" fill="none" stroke="var(--blue)" stroke-width="1.5"/>
    <path d="M20 150 C60 190 40 260 100 300 C140 326 160 350 180 380" fill="none" stroke="var(--orange)" stroke-width="1.5"/>
    <path d="M860 380 C880 330 930 300 1010 290 L1010 380 Z" fill="var(--orange)"/>
    <path d="M1010 190 C960 230 950 300 900 340 C880 355 870 370 860 380" fill="none" stroke="var(--blue)" stroke-width="1.5"/>
    <path d="M1010 230 C980 260 970 310 930 340" fill="none" stroke="var(--orange)" stroke-width="1.5"/>

    <!-- brand -->
    <rect x="10" y="26" width="30" height="30" fill="var(--green-ink)"/>
    <text class="brand-credit" x="48" y="31">Dr. Anna Fernlow (MBBS, MD)</text>
    <text class="brand-name" x="48" y="50">VERDANT CARE HUB</text>
    <text class="brand-tagline" x="48" y="62">Natural Healing and Integrative Wellness</text>

    <text class="section-title" x="505" y="126" text-anchor="middle">OUR SERVICES</text>

    <!-- services -->
    <g class="service" transform="translate(188 0)">
      <text class="service-label" x="0" y="183" text-anchor="middle">CHELATION</text>
      <text class="service-label" x="0" y="196" text-anchor="middle">THERAPY</text>
      <rect x="-10" y="205" width="20" height="8" fill="var(--blue)"/>
      <path d="M-37 218 Q-37 211 -30 211 L30 211 Q37 211 37 218 L37 298 L22 317 L-22 317 L-37 298 Z" fill="var(--blue)"/>
      <path d="M-32 220 L32 220 L32 296 L20 311 L-20 311 L-32 296 Z" fill="url(#fill-chelation)" role="img" aria-label="Photo of a glowing human heart"/>
      <line x1="0" y1="317" x2="0" y2="380" stroke="var(--blue)" stroke-width="3"/>
      <rect x="-7" y="333" width="14" height="24" fill="var(--blue)"/>
    </g>
    <g class="service" transform="translate(314 0)">
      <text class="service-label" x="0" y="183" text-anchor="middle">IV VITAMIN C</text>
      <text class="service-label" x="0" y="196" text-anchor="middle">THERAPY</text>
      <rect x="-10" y="205" width="20" height="8" fill="var(--orange)"/>
      <path d="M-37 218 Q-37 211 -30 211 L30 211 Q37 211 37 218 L37 298 L22 317 L-22 317 L-37 298 Z" fill="var(--orange)"/>
      <path d="M-32 220 L32 220 L32 296 L20 311 L-20 311 L-32 296 Z" fill="url(#fill-vitamin)" role="img" aria-label="Photo of sliced oranges"/>
      <line x1="0" y1="317" x2="0" y2="380" stroke="var(--orange)" stroke-width="3"/>
      <rect x="-7" y="333" width="14" height="24" fill="var(--orange)"/>
    </g>
    <g class="service" transform="translate(440 0)">
      <text class="service-label" x="0" y="183" text-anchor="middle">IV NUTRITION</text>
      <text class="service-label" x="0" y="196" text-anchor="middle">THERAPY</text>
      <rect x="-10" y="205" width="20" height="8" fill="var(--blue)"/>
      <path d="M-37 218 Q-37 211 -30 211 L30 211 Q37 211 37 218 L37 298 L22 317 L-22 317 L-37 298 Z" fill="var(--blue)"/>
      <path d="M-32 220 L32 220 L32 296 L20 311 L-20 311 L-32 296 Z" fill="url(#fill-nutrition)" role="img" aria-label="Photo of fresh fruits and vegetables"/>
      <line x1="0" y1="317" x2="0" y2="380" stroke="var(--blue)" stroke-width="3"/>
      <rect x="-7" y="333" width="14" height="24" fill="var(--blue)"/>
    </g>
    <g class="service" transform="translate(564 0)">
      <text class="service-label" x="0" y="189" text-anchor="middle">HOMEOPATHY</text>
      <rect x="-10" y="205" width="20" height="8" fill="var(--orange)"/>
      <path d="M-37 218 Q-37 211 -30 211 L30 211 Q37 211 37 218 L37 298 L22 317 L-22 317 L-37 298 Z" fill="var(--orange)"/>
      <path d="M-32 220 L32 220 L32 296 L20 311 L-20 311 L-32 296 Z" fill="url(#fill-homeopathy)" role="img" aria-label="Photo of glass vials of homeopathic pills"/>
      <line x1="0" y1="317" x2="0" y2="380" stroke="var(--orange)" stroke-width="3"/>
      <rect x="-7" y="333" width="14" height="24" fill="var(--orange)"/>
    </g>
    <g class="service" transform="translate(695 0)">
      <text class="service-label" x="0" y="189" text-anchor="middle">ACUPUNCTURE</text>
      <rect x="-10" y="205" width="20" height="8" fill="var(--blue)"/>
      <path d="M-37 218 Q-37 211 -30 211 L30 211 Q37 211 37 218 L37 298 L22 317 L-22 317 L-37 298 Z" fill="var(--blue)"/>
      <path d="M-32 220 L32 220 L32 296 L20 311 L-20 311 L-32 296 Z" fill="url(#fill-acupuncture)" role="img" aria-label="Photo of acupuncture needles placed in skin"/>
      <line x1="0" y1="317" x2="0" y2="380" stroke="var(--blue)" stroke-width="3"/>
      <rect x="-7" y="333" width="14" height="24" fill="var(--blue)"/>
    </g>
    <g class="service" transform="translate(822 0)">
      <text class="service-label" x="0" y="189" text-anchor="middle">AYURVEDA</text>
      <rect x="-10" y="205" width="20" height="8" fill="var(--orange)"/>
      <path d="M-37 218 Q-37 211 -30 211 L30 211 Q37 211 37 218 L37 298 L22 317 L-22 317 L-37 298 Z" fill="var(--orange)"/>
      <circle cx="0" cy="265" r="19" fill="none" stroke="var(--white)" stroke-width="3"/>
      <path d="M0 249 A16 16 0 0 1 0 281 A8 8 0 0 1 0 265 A8 8 0 0 0 0 249 Z" fill="var(--white)"/>
      <circle cx="0" cy="257" r="2.5" fill="var(--white)"/>
      <circle cx="0" cy="273" r="2.5" fill="var(--orange)"/>
      <line x1="0" y1="317" x2="0" y2="380" stroke="var(--orange)" stroke-width="3"/>
      <rect x="-7" y="333" width="14" height="24" fill="var(--orange)"/>
    </g>
  </svg>
</section>
</body>
</html>
```